Pella Acupuncture Business Card Design

I would like a business card design for my acupuncture business which is based from 2 practices in Melbourne, Australia.

The front of the card should include:

*The Logo
* Name - Miranda Tovelisca (B.App.Sc.(TCM), Dip.Rem.Mass.). (I would like the letters after my name in slightly smaller font)
* Mobile number - 0472 318 604
* Web address - www.pellaacupuncture-example.com.au

On the back of the card I would somehow like to fit my 2 clinic addresses in. They are:

The Birchwood Restoration Rooms
842 Fennimore Rd, Camberwell VIC 3124
Ph: 1300 274 518

Quillbrook Integrative & Eastern Herbal Therapy Clinic
31 Marlowby Rd, Malvern East VIC 3145
Ph: (03) 9871 3352

If there is space, I'd also like to add to the back of the card - Next Appointment............................ (or something along those lines).

Thanks and happy designing!

Target Market(s)

Health consumers, and colleagues in the health industry

Industry/Entity Type

Clinic

Contact Information for Business Card

as above in brief

Requirements
Must have
• I've seen some ok designs coming in, however I'd like to avoid the generic look with the added curved line details etc. I don't particularly need extra patterns added to the card. I'd prefer it to look quite clean and simple, and using more earthy colours (I'm not super keen on the lime green that a lot of designs seem to include. I don't mind the full black or white look, (obviously the back side needs to be a lighter colour to allow me to write appointment details on it). I also quite like the idea of the background looking like brown recycled paper (just an idea - that's not 100% necessary).
Nice to have
• I have an idea that I could have the main flower part of the logo printed as metallic.
Should not have
• Generic patterns and too much added detail.

```html
<!DOCTYPE html>
<html lang="en">
<head>
<meta charset="utf-8">
<title>Pella Acupuncture – Business Card</title>
<link rel="stylesheet" href="https://fonts.googleapis.com/css2?family=Open+Sans:wght@400;600;700&display=swap">
<style>
  :root {
    --backdrop: #e7e4df;
    --card-black: #121110;
    --card-sheen: #2a2724;
    --kraft: #d8c6a5;
    --kraft-deep: #c9b48f;
    --ink-dark: #3a2e24;
    --ink-soft: #6a5a4a;
    --ink-light: #ece6dc;
    --accent-olive: #5f6b34;
    --metal-gold: #b99a5b;
    --icon-clay: #9a5a3c;
  }
  * { box-sizing: border-box; margin: 0; padding: 0; }
  html, body {
    width: 1200px; height: 913px; overflow: hidden;
    background: var(--backdrop);
    font-family: "Open Sans", Arial, sans-serif;
  }
  .stage { position: relative; width: 1200px; height: 913px; }

  .card {
    position: absolute;
    width: 520px; height: 317px;
    border-radius: 4px;
    box-shadow: 0 12px 28px rgba(0,0,0,.25);
    overflow: hidden;
  }
  .card--front {
    left: 60px; top: 130px;
    background: linear-gradient(135deg, var(--card-sheen) 0%, var(--card-black) 45%, var(--card-black) 100%);
    color: var(--ink-light);
  }
  .card--back {
    left: 620px; top: 466px;
    background: linear-gradient(160deg, var(--kraft) 0%, var(--kraft-deep) 100%);
    color: var(--ink-dark);
  }

  .brand { display: flex; align-items: center; gap: 12px; }
  .brand__disc {
    border-radius: 50%;
    background: radial-gradient(circle at 35% 30%, #e2cc96 0%, var(--metal-gold) 60%, #8c7140 100%);
    flex: none;
  }
  .brand__name { font-weight: 600; white-space: nowrap; }

  .card--front .brand {
    position: absolute; left: 50%; top: 50%; transform: translate(-50%, -50%);
  }
  .card--front .brand__disc { width: 46px; height: 46px; }
  .card--front .brand__name { font-size: 30px; letter-spacing: .5px; color: var(--ink-light); }

  .card--back .brand {
    position: absolute; left: 18px; top: 100px; width: 124px;
    flex-direction: column; gap: 8px;
  }
  .card--back .brand__disc { width: 40px; height: 40px; }
  .card--back .brand__name { font-size: 14px; color: var(--ink-dark); }

  .contact { position: absolute; left: 168px; top: 26px; right: 16px; }
  .contact__name { font-size: 16px; font-weight: 700; color: var(--accent-olive); line-height: 21px; }
  .contact__quals { font-size: 10px; color: var(--ink-soft); margin-bottom: 6px; }
  .contact__line {
    display: flex; align-items: center; gap: 8px;
    font-size: 11px; line-height: 18px; white-space: nowrap;
  }
  .contact__icon { width: 12px; height: 12px; flex: none; }

  .clinics { position: absolute; left: 150px; right: 16px; top: 138px; text-align: right; }
  .clinic { margin-bottom: 9px; }
  .clinic__title { font-size: 10px; font-weight: 700; color: var(--accent-olive); white-space: nowrap; line-height: 15px; }
  .clinic__title::after { content: " «"; }
  .clinic__address { font-size: 10px; color: var(--ink-dark); white-space: nowrap; line-height: 15px; }

  .appointment {
    position: absolute; left: 18px; right: 16px; bottom: 26px;
    display: flex; align-items: flex-end; gap: 8px;
    font-size: 11px; font-weight: 600; color: var(--ink-dark);
  }
  .appointment__rule {
    flex: 1; border-bottom: 1.5px dotted var(--ink-soft); margin-bottom: 3px;
  }
</style>
</head>
<body>
<main class="stage">

  <section class="card card--front" aria-label="Business card front">
    <div class="brand">
      <span class="brand__disc"></span>
      <span class="brand__name">Pella Acupuncture</span>
    </div>
  </section>

  <section class="card card--back" aria-label="Business card back">
    <div class="brand">
      <span class="brand__disc"></span>
      <span class="brand__name">Pella Acupuncture</span>
    </div>

    <div class="contact">
      <p class="contact__name">Miranda Tovelisca</p>
      <p class="contact__quals">B.App.Sc.(TCM), Dip.Rem.Mass.</p>
      <p class="contact__line">
        <svg class="contact__icon" viewBox="0 0 12 12" aria-hidden="true">
          <circle cx="6" cy="6" r="6" fill="var(--icon-clay)"/>
          <path d="M3.6 3.2 L4.8 3 L5.4 4.4 L4.7 5 Q5.3 6.4 6.9 7.3 L7.5 6.6 L8.9 7.2 L8.7 8.4 Q5.4 8.6 3.6 3.2Z" fill="#fff"/>
        </svg>
        0472 318 604
      </p>
      <p class="contact__line">
        <svg class="contact__icon" viewBox="0 0 12 12" aria-hidden="true">
          <circle cx="6" cy="6" r="6" fill="var(--icon-clay)"/>
          <rect x="3" y="4" width="6" height="4.2" fill="#fff"/>
          <path d="M3 4 L6 6.4 L9 4" fill="none" stroke="var(--icon-clay)" stroke-width=".7"/>
        </svg>
        hello@pellaacupuncture-example.com.au
      </p>
      <p class="contact__line">
        <svg class="contact__icon" viewBox="0 0 12 12" aria-hidden="true">
          <circle cx="6" cy="6" r="6" fill="var(--accent-olive)"/>
          <circle cx="6" cy="6" r="3.4" fill="none" stroke="#fff" stroke-width=".8"/>
          <path d="M2.6 6 H9.4 M6 2.6 V9.4" stroke="#fff" stroke-width=".7"/>
        </svg>
        www.pellaacupuncture-example.com.au
      </p>
    </div>

    <div class="clinics">
      <div class="clinic">
        <p class="clinic__title">The Birchwood Restoration Rooms</p>
        <p class="clinic__address">842 Fennimore Rd, Camberwell VIC 3124 • Ph: 1300 274 518</p>
      </div>
      <div class="clinic">
        <p class="clinic__title">Quillbrook Integrative &amp; Eastern Herbal Therapy Clinic</p>
        <p class="clinic__address">31 Marlowby Rd, Malvern East VIC 3145 • Ph: (03) 9871 3352</p>
      </div>
    </div>

    <div class="appointment">
      <span>Next Appointment</span>
      <span class="appointment__rule"></span>
    </div>
  </section>

</main>
</body>
</html>
```